Pool Up, Pay Less! Innovative Team Buying Web App

Pooli is a team-buying/social commerce web app that is a cross between Bundlora and sites/apps like Kivo, Marlix, and Fenxiangtuo. It is basically like a game in which users seek to get the lowest prices by working with friends and neighbours (as a team) to maximize order volumes. Sellers on the platform set volume targets which teams have to hit to secure wholesale price.
We need a landing page and a few (4 - 5) key pages that project a compelling game-like aesthetic that is innovative and playful, while being clean and classy.

Target Market(s)

Nigerian homemakers. Typically 30+ years old. Predominantly female, middle class.

Industry/Entity Type

Ecommerce, Groceries.

Coding

Coded - Design and coding required

Number of Pages Required

5+ page

Requirements
Must have
• PAGES (1). Landing page. An attractive landing page that gives a brief overview of the concept and main features. We are going to roll out an MVP with just the landing page (which should include a sign-up form) so this page is critical and should be "self-contained" with it's signup inputs. The signup section must include a referral code so that we can track who referred whom. (2). Available deals. A listing of all active deals with enough relevant information. Note that deals have a deadline, a retail price, and a minimum volume target to unlock wholesale price. (3). Deal details page. This should show the standard price (the price the user would pay if he buys a small quantity), team price (the wholesale price based on the team hitting the required order volume), the points to be earned by buying the item, etc. (4). Checkout page. In addition to normal checkout stuff on this page the user can convert points into currency (at an exchange rate that may vary from time to time). Example: if price is $3,000 he may see that he has 1000 points in his wallet and the exchange rate is 1:1, so he can go ahead and convert to $1,000 and the price now becomes $2,000. (5). Profile page. Where the user can see things like his performance (how his points were calculated), his lineage ("children" and "grandchildren"), points required to get to the next rank, his order history, etc.
Nice to have
• GUIDELINES (1). Overall Aesthetic is game-like: playful, bright, and colourful. But clean and classic at the same time: we don't want a look that goes "out of fashion" within the next two or three years. (2). Referral is critical. Therefore the "Share" button (or whatever) should be easily accessible and visible on all relevant pages. (3). The user's community is critical. Therefore the activity of the users "network" (the "children" and "grandchildren") must be somehow dynamically visible at most/all times. We want to project a sense of realtime dynamism, just like a game. The user should be able to somehow "see" things happening in the network (e.g. when someone in his network buys something). (4). Like a game, the user's points, rank, and badges must always/usually be visible and we need an interesting visual effect when something happens that increases his points. Examples of actions that generate points include buying an item, when a "child" or "grandchild" buys an item, when someone you invited/referred creates an account, etc. We need a clear idea of the visual effect and how it would work.

```html
<!DOCTYPE html>
<html lang="en">
<head>
<meta charset="utf-8">
<title>Pooli – Pool Up, Pay Less!</title>
<link href="https://fonts.googleapis.com/css2?family=Poppins:ital,wght@0,400;0,500;0,600;0,700;1,400&display=swap" rel="stylesheet">
<style>
:root{
  --ink:#2b2b2b;
  --white:#ffffff;
  --yellow:#fff200;
  --hero-deep:#062a7a;
  --hero-bright:#1560e6;
  --purple:#a50fe8;
  --frame-yellow:#ffd500;
  --process-blue:#2424de;
  --card-amber:#ffbb00;
  --card-orange:#ff4d0a;
  --card-cyan:#0cc3e8;
  --accent-blue:#2424de;
  --green:#5db50f;
  --green-dark:#3e8a08;
  --coral:#f25456;
  --news-blue:#1590e6;
  --news-dark:#0b62b5;
  --footer:#333333;
  --footer-line:#4a4a4a;
  --q-pink:#f0c3e0;
  --q-purple:#8a33d6;
  --q-green:#a9cf6a;
  --q-orange:#f4ad5c;
}
*{margin:0;padding:0;box-sizing:border-box}
html,body{width:1200px;height:3978px;overflow:hidden}
body{font-family:'Poppins',sans-serif;color:var(--ink);background:var(--white)}
.page{position:relative;width:1200px;height:3978px;overflow:hidden}
.abs{position:absolute}
.btn{position:absolute;display:flex;align-items:center;justify-content:center;font-weight:700;font-size:20px;text-decoration:none;font-family:'Poppins',sans-serif;border:0;cursor:pointer}
.btn--yellow{background:var(--yellow);color:#111}
.btn--outline{border:2px solid var(--white);color:var(--white);background:transparent}

/* header */
.site-header{top:0;left:0;width:1200px;height:91px;background:var(--white)}
.brand{position:absolute;left:74px;top:28px;font-size:30px;font-weight:700;color:#555;letter-spacing:1px}
.main-nav{position:absolute;right:74px;top:36px;display:flex;gap:40px;font-size:17px;color:#333}

/* hero */
.hero{top:91px;left:0;width:1200px;height:647px;background:radial-gradient(ellipse at 70% 40%,var(--hero-bright) 0%,#0d46c4 45%,var(--hero-deep) 100%);color:var(--white)}
.hero__kicker{position:absolute;left:74px;top:90px;font-size:22px;font-weight:600}
.hero__title{position:absolute;left:74px;top:116px;font-size:74px;line-height:72px;font-weight:700}
.hero__text{position:absolute;left:74px;top:290px;width:420px;font-size:19px;line-height:35px}
.collage{position:absolute;background:var(--white);padding:6px;display:grid;grid-template-columns:1fr 1fr;grid-template-rows:1fr 1fr;gap:6px}
.collage span:nth-child(1){background:var(--q-pink)}
.collage span:nth-child(2){background:var(--q-purple)}
.collage span:nth-child(3){background:var(--q-green)}
.collage span:nth-child(4){background:var(--q-orange)}

/* about */
.about-box{left:74px;top:783px;width:513px;height:489px;background:var(--purple);color:var(--white)}
.about-box h2{position:absolute;left:34px;top:56px;font-size:49px;line-height:46px;font-weight:700}
.about-box p{position:absolute;left:34px;top:166px;width:390px;font-size:17px;line-height:31.5px}
.about-frame{left:784px;top:880px;width:351px;height:298px;border-top:7px solid var(--frame-yellow);border-right:7px solid var(--frame-yellow)}
.about-photo{left:525px;top:889px;width:601px;height:515px;background:linear-gradient(135deg,#d9d3c8,#9e8b76 55%,#5d5048)}

/* process */
.process-band{left:0;top:1498px;width:1200px;height:522px;background:var(--process-blue)}
.process-title{left:0;top:1570px;width:1200px;text-align:center;color:var(--white);font-size:52px;font-weight:700}
.step{top:1692px;width:329px;height:413px;overflow:hidden;color:var(--white)}
.step--1{left:74px;background:var(--card-amber)}
.step--2{left:437px;background:var(--card-orange)}
.step--3{left:798px;background:var(--card-cyan)}
.step__num{position:absolute;right:14px;bottom:-40px;font-size:200px;font-weight:700;line-height:1;color:rgba(255,255,255,.22)}
.step__text{position:absolute;left:25px;top:182px;width:290px;font-size:31px;line-height:41px;font-weight:700}
.step__text em{font-style:normal;text-decoration:underline;text-underline-offset:8px;text-decoration-thickness:2px}
.step--1 em{color:var(--accent-blue)}
.step--2 em,.step--3 em{color:var(--yellow)}

/* testimonial */
.testimonial-shape{left:0;top:2140px}
.quote-mark{left:112px;top:2176px;font-size:110px;line-height:1;font-weight:700;color:rgba(255,255,255,.35);font-family:Georgia,serif}
.quote-text{left:123px;top:2228px;width:600px;font-size:18px;line-height:30px;font-style:italic;color:var(--white)}
.quote-name{left:123px;top:2386px;font-size:23px;font-weight:700;color:var(--white)}
.testimonial-photo{left:726px;top:2208px;width:416px;height:340px;background:linear-gradient(160deg,#6b4b3c,#d6a0a8 60%,#e8b9be);border-radius:40% 40% 0 0}

/* get started */
.cta{left:0;top:2651px;width:1200px;height:456px;background:var(--coral);color:var(--white)}
.cta h2{position:absolute;left:74px;top:88px;font-size:50px;font-weight:700}
.cta p{position:absolute;left:74px;top:162px;width:470px;font-size:23px;line-height:36px}

/* sign-up */
.news-shape{left:0;top:3140px}
.news-title{left:0;top:3224px;width:1200px;text-align:center;color:var(--white);font-size:52px;font-weight:700}
.news-sub{left:0;top:3310px;width:1200px;text-align:center;color:var(--white);font-size:22px}
.signup-form{left:289px;top:3369px;width:627px;height:57px}
.field{position:absolute;top:0;height:57px;border:2px solid var(--white);background:transparent;color:var(--white);font-family:'Poppins',sans-serif;font-size:17px;padding-left:20px}
.field::placeholder{color:var(--white);opacity:1}
.field--email{left:0;width:262px}
.field--ref{left:274px;width:157px;padding-left:16px}

/* footer */
.site-footer{left:0;top:3670px;width:1200px;height:308px;background:var(--footer);color:var(--white)}
.footer-col{position:absolute;top:71px}
.footer-col h3{font-size:16px;font-weight:700;letter-spacing:.3px;margin-bottom:10px}
.footer-col li{list-style:none;font-size:15px;line-height:32.5px}
.store-badge{position:absolute;left:883px;width:155px;height:49px;border:2px solid #cfcfcf;border-radius:7px;background:#111}
.footer-line{position:absolute;left:0;top:247px;width:1200px;height:1px;background:var(--footer-line)}
.copyright{position:absolute;left:77px;top:270px;font-size:14px}
.socials{position:absolute;left:970px;top:262px;display:flex;gap:7px}
.socials span{width:34px;height:34px;border-radius:50%;background:var(--white)}
</style>
</head>
<body>
<div class="page">

  <header class="abs site-header">
    <div class="brand">POOLI</div>
    <nav class="main-nav"><span>Available deals</span><span>Deal details</span><span>Checkout</span><span>Profile</span></nav>
  </header>

  <section class="abs hero">
    <div class="hero__kicker">Pool Up, Pay Less!</div>
    <h1 class="hero__title">Build great<br>teams</h1>
    <p class="hero__text">Pooli is team buying with superpowers. Shop with friends and neighbours, hit seller volume targets, unlock wholesale prices, earn points and much more...</p>
    <a class="btn btn--yellow" style="left:74px;top:496px;width:179px;height:57px">Request Demo</a>
    <a class="btn btn--outline" style="left:272px;top:496px;width:128px;height:57px">Sign Up</a>
    <div class="collage" role="img" aria-label="App screens: available deals, team progress, points wallet and checkout" style="left:522px;top:144px;width:605px;height:358px">
      <span></span><span></span><span></span><span></span>
    </div>
  </section>

  <div class="abs about-photo" role="img" aria-label="Family laughing together on a sofa around a phone"></div>
  <div class="abs about-frame"></div>
  <section class="abs about-box">
    <h2>About<br>Our Company</h2>
    <p>Sed ut perspiciatis unde omnis iste natus error sit voluptatem accusantium doloremque laudantium, totam rem aperiam, eaque ipsa quae ab illo inventore veritatis et quasi architecto beatae vitae dicta sunt explicabo sed quia consequuntur magni dolores eos qui dolore magnam aliquam quaerat voluptatem.</p>
  </section>
  <a class="btn btn--yellow" style="left:91px;top:1243px;width:179px;height:59px">Read More</a>

  <div class="abs process-band"></div>
  <h2 class="abs process-title">Our Process</h2>
  <div class="abs step step--1"><span class="step__num">1</span><p class="step__text"><em>Parent</em> is the person who starts the team and shares the deal</p></div>
  <div class="abs step step--2"><span class="step__num">2</span><p class="step__text"><em>Children</em> join the team using the parent's referral code</p></div>
  <div class="abs step step--3"><span class="step__num">3</span><p class="step__text"><em>Grand child</em> is the next person who joins using a child's referral</p></div>

  <svg class="abs testimonial-shape" width="1200" height="460" viewBox="0 0 1200 460" aria-hidden="true">
    <polygon points="74,320 1127,404 1056,438" fill="var(--green-dark)"/>
    <polygon points="74,22 1085,50 1127,404 74,328" fill="var(--green)"/>
  </svg>
  <div class="abs testimonial-photo" role="img" aria-label="Cheerful woman holding a smartphone"></div>
  <div class="abs quote-mark">“</div>
  <p class="abs quote-text">Sed ut perspiciatis unde omnis iste natus error sit voluptatem accusantium doloremque laudantium, totam rem aperiam, eaque ipsa quae ab illo inventore veritatis et quasi architecto beatae vitae dicta sunt explicabo sed quia consequuntur magni dolores eos qui dolore magnam aliquam quaerat voluptatem...”</p>
  <div class="abs quote-name">Name Heading</div>
  <svg class="abs" style="left:123px;top:2424px" width="140" height="22" viewBox="0 0 140 22" role="img" aria-label="Five stars">
    <g fill="var(--yellow)">
      <polygon points="10,1 13,8 20,8 14.5,12.5 16.5,20 10,15.5 3.5,20 5.5,12.5 0,8 7,8"/>
      <polygon transform="translate(29 0)" points="10,1 13,8 20,8 14.5,12.5 16.5,20 10,15.5 3.5,20 5.5,12.5 0,8 7,8"/>
      <polygon transform="translate(58 0)" points="10,1 13,8 20,8 14.5,12.5 16.5,20 10,15.5 3.5,20 5.5,12.5 0,8 7,8"/>
      <polygon transform="translate(87 0)" points="10,1 13,8 20,8 14.5,12.5 16.5,20 10,15.5 3.5,20 5.5,12.5 0,8 7,8"/>
      <polygon transform="translate(116 0)" points="10,1 13,8 20,8 14.5,12.5 16.5,20 10,15.5 3.5,20 5.5,12.5 0,8 7,8"/>
    </g>
  </svg>

  <section class="abs cta">
    <h2>Get Started Today</h2>
    <p>Pooli is free and easy-to-use.<br>Why pay retail when your team can buy at wholesale prices?</p>
    <a class="btn btn--yellow" style="left:74px;top:295px;width:179px;height:57px">Request Demo</a>
    <a class="btn btn--outline" style="left:272px;top:295px;width:274px;height:57px">Download Mobile App</a>
    <div class="collage" role="img" aria-label="App screens: available deals, team progress, points wallet and checkout" style="left:599px;top:66px;width:550px;height:325px">
      <span></span><span></span><span></span><span></span>
    </div>
  </section>

  <svg class="abs news-shape" width="1200" height="450" viewBox="0 0 1200 450" aria-hidden="true">
    <polygon points="147,434 1127,331 1127,345 150,444" fill="var(--news-dark)"/>
    <polygon points="116,45 1127,14 1127,331 74,419" fill="var(--news-blue)"/>
  </svg>
  <h2 class="abs news-title">Join Your Team Today</h2>
  <p class="abs news-sub">Sign up with a referral code and start saving.</p>
  <form class="abs signup-form" action="#">
    <input class="field field--email" type="email" name="email" placeholder="Email Address" aria-label="Email Address">
    <input class="field field--ref" type="text" name="referral" placeholder="Referral Code" aria-label="Referral Code">
    <button class="btn btn--yellow" type="submit" style="left:448px;top:0;width:179px;height:57px">Sign Up</button>
  </form>

  <footer class="abs site-footer">
    <div class="footer-col" style="left:77px"><h3>QUICK LINKS</h3><ul><li>Available deals</li><li>Deal details</li><li>Checkout</li><li>Profile</li></ul></div>
    <div class="footer-col" style="left:344px"><h3>COMPANY</h3><ul><li>Contact Us</li><li>Legal</li></ul></div>
    <div class="footer-col" style="left:618px"><h3>RESOURCES</h3><ul><li>Product Support</li><li>Request a Demo</li><li>Online Demos</li></ul></div>
    <div class="footer-col" style="left:883px"><h3>DOWNLOAD THE APP</h3></div>
    <div class="store-badge" style="top:102px" role="img" aria-label="App store badge"></div>
    <div class="store-badge" style="top:155px" role="img" aria-label="App store badge"></div>
    <div class="footer-line"></div>
    <div class="copyright">Copyright © 2023 CompanyName .All Right Reserved</div>
    <div class="socials" aria-label="Social links"><span></span><span></span><span></span><span></span></div>
  </footer>

</div>
</body>
</html>
```